Verdant Grain Collective needs packaging design for 500g Hemp Seed Pouch

We need a packaging design for the release of our Australian sourced Super Healthy, Nutritious super food HEMP SEED.

The verdant Grain collective - food, fibre, fuel, building, medicine
We are a start up company who is very Passionate about Hemp, rebuilding the hemp industry through inspiration, education and distribution of all things hemp.

This Hemp Seed packaging will be our first product launch

Kernel of FIELD SEEDS 500gram

needs to communicate 3 things, that Hemp seeds:
1. TASTE GREAT
2. EASY TO USE
3. GOOD FOR YOU

other Features of hemp seeds is that they are :
Vegan
Paleo
Raw
Sustainable
High in protein
High in Omega 3 + 6 EFA
Anti allergenic

we would like to see designs that work with our current logo and colouring of orange and black. premium and stylish that says healthy

the pouches will be '500g' meaning they will hold 500grams of hulled hemp seeds.

with dimensions of
170mm x 250mm
see attached photo of competitors hemp protein pouch as example of pouch design

see attached for current logo designs and colouring
also see attached concept sketch we are not married to this sketch it is just as a guideline for elements that should be included.

final design should feel healthy clean and safe for consumption:)
with an emphasis on being PremiumAustralian seed soured from from pristine Tasmania

Target Market(s)

Health conscious

Requirements
Must have
• map of Australia or show that it is Australian in some way
Nice to have
• Spoon of hemp seeds or picture of Grain Cores

```html
<!DOCTYPE html>
<html lang="en">
<head>
<meta charset="utf-8">
<title>Kernel of Field Seeds – 500g Pouch Label</title>
<link rel="stylesheet" href="https://fonts.googleapis.com/css2?family=Sniglet&family=Libre+Franklin:wght@500;600;700;800&family=Montserrat:wght@500;600;700&display=swap">
<style>
  :root {
    --bg: #e9e6e1;
    --paper: #ffffff;
    --orange: #f4a231;
    --green: #4b9b38;
    --ink: #1b1b1b;
    --muted-green: #dfe8d8;
  }
  * { box-sizing: border-box; margin: 0; padding: 0; }
  html, body { width: 1200px; height: 900px; overflow: hidden; }
  body { background: var(--bg); font-family: "Montserrat", sans-serif; color: var(--ink); }

  .label {
    position: absolute; left: 342px; top: 62px;
    width: 516px; height: 775px;
    background: var(--paper); overflow: hidden;
  }
  .top-band { position: absolute; left: 0; top: 0; width: 516px; height: 112px; }
  .tagline {
    position: absolute; left: 0; top: 38px; width: 100%;
    text-align: center; color: #fff;
    font-family: "Sniglet", sans-serif; font-size: 28px; letter-spacing: 0.3px;
  }

  .brand { position: absolute; left: 46px; top: 118px; display: flex; align-items: center; gap: 10px; }
  .brand-dot { width: 22px; height: 22px; border-radius: 50%; border: 3px solid var(--ink); }
  .brand-name { font-family: "Libre Franklin", sans-serif; font-weight: 700; font-size: 15px; color: var(--ink); line-height: 1.2; width: 120px; }

  .nutrition { position: absolute; left: 335px; top: 146px; width: 157px; color: #fff; }
  .nutrition-head { background: var(--orange); font-size: 10.5px; font-weight: 500; padding: 5px 8px; height: 22px; }
  .nutrition-table { background: var(--orange); margin-top: 5px; padding: 5px 8px; font-size: 10.5px; font-weight: 500; }
  .nutrition-row { display: flex; line-height: 16px; }
  .nutrition-row span:first-child { width: 66px; }

  .illustration {
    position: absolute; left: 225px; top: 270px; width: 291px; height: 505px;
    background: radial-gradient(ellipse at 55% 35%, var(--muted-green) 0%, #f1f5ee 55%, var(--paper) 80%);
  }

  .title { position: absolute; left: 44px; top: 278px; font-family: "Libre Franklin", sans-serif; }
  .title-small { font-size: 25px; font-weight: 600; line-height: 28px; letter-spacing: -0.3px; }
  .title-big { font-size: 58px; font-weight: 600; line-height: 56px; letter-spacing: -1px; }
  .title-orange { color: var(--orange); }
  .title-green { color: var(--green); }

  .subline { position: absolute; left: 44px; top: 417px; width: 206px; }
  .dots { border-top: 4px dotted var(--ink); height: 0; }
  .subline-text { font-family: "Libre Franklin", sans-serif; font-weight: 600; font-size: 13px; line-height: 18px; padding: 6px 0 6px; }

  .features { position: absolute; left: 46px; top: 500px; list-style: none; }
  .features li { display: flex; align-items: center; gap: 8px; font-family: "Libre Franklin", sans-serif; font-weight: 600; font-size: 12.5px; line-height: 17px; }
  .tick { width: 12px; height: 12px; }

  .net-weight { position: absolute; left: 66px; top: 633px; font-family: "Libre Franklin", sans-serif; font-weight: 800; }
  .net-weight-label { font-size: 15px; }
  .net-weight-value { font-size: 21px; font-weight: 700; }

  .badges { position: absolute; left: 32px; top: 705px; display: flex; align-items: center; gap: 14px; }
  .badge-round { width: 62px; height: 62px; border-radius: 50%; border: 3px solid var(--orange); }
  .badge-cert { width: 100px; height: 42px; border: 2px solid var(--green); border-radius: 6px; }
  .origin-map { width: 50px; height: 44px; background: linear-gradient(135deg, #3a5fae, #c8323a); border-radius: 6px; }
  .origin-text { font-family: "Libre Franklin", sans-serif; font-weight: 600; font-size: 10px; line-height: 13px; }
</style>
</head>
<body>
  <main class="label">
    <svg class="top-band" viewBox="0 0 516 112" aria-hidden="true">
      <path d="M0 0 H516 V86 Q258 118 0 86 Z" fill="var(--orange)"/>
    </svg>
    <p class="tagline">Natures Perfect SuperFood</p>

    <div class="brand">
      <span class="brand-dot"></span>
      <span class="brand-name">Verdant Grain Collective</span>
    </div>

    <section class="nutrition">
      <div class="nutrition-head">NUTRITION / TBSP (20g)</div>
      <div class="nutrition-table">
        <div class="nutrition-row"><span>2.0 g</span><span>Omega-3</span></div>
        <div class="nutrition-row"><span>6.4 g</span><span>Protein</span></div>
        <div class="nutrition-row"><span>2.1 mg</span><span>Iron</span></div>
        <div class="nutrition-row"><span>12.8 mg</span><span>Magnesium</span></div>
      </div>
    </section>

    <div class="illustration" role="img" aria-label="Line drawing of a flowering seed plant with leaves and stems"></div>

    <h1 class="title">
      <span class="title-small" style="display:block">KERNEL OF</span>
      <span class="title-big title-orange" style="display:block">FIELD</span>
      <span class="title-big title-green" style="display:block">SEEDS</span>
    </h1>

    <div class="subline">
      <div class="dots"></div>
      <p class="subline-text">HIGH NUTRITION FOR YOUR FAVOURITE FOOD</p>
      <div class="dots"></div>
    </div>

    <ul class="features">
      <li><svg class="tick" viewBox="0 0 12 12"><path d="M1 6.5 L4.5 10 L11 1.5" fill="none" stroke="var(--orange)" stroke-width="2"/></svg>VEGAN</li>
      <li><svg class="tick" viewBox="0 0 12 12"><path d="M1 6.5 L4.5 10 L11 1.5" fill="none" stroke="var(--orange)" stroke-width="2"/></svg>PALEO</li>
      <li><svg class="tick" viewBox="0 0 12 12"><path d="M1 6.5 L4.5 10 L11 1.5" fill="none" stroke="var(--orange)" stroke-width="2"/></svg>RAW</li>
      <li><svg class="tick" viewBox="0 0 12 12"><path d="M1 6.5 L4.5 10 L11 1.5" fill="none" stroke="var(--orange)" stroke-width="2"/></svg>SUSTAINABLE</li>
      <li><svg class="tick" viewBox="0 0 12 12"><path d="M1 6.5 L4.5 10 L11 1.5" fill="none" stroke="var(--orange)" stroke-width="2"/></svg>HIGH PROTEIN</li>
      <li><svg class="tick" viewBox="0 0 12 12"><path d="M1 6.5 L4.5 10 L11 1.5" fill="none" stroke="var(--orange)" stroke-width="2"/></svg>ANTI - ALERGIC</li>
    </ul>

    <div class="net-weight">
      <div class="net-weight-label">NET WT.</div>
      <div class="net-weight-value">500g</div>
    </div>

    <div class="badges">
      <span class="badge-round"></span>
      <span class="badge-cert"></span>
      <span class="origin-map" role="img" aria-label="Map of Australia in national flag colours"></span>
      <span class="origin-text">PREMIUM<br>TASMANIAN<br>SEED</span>
    </div>
  </main>
</body>
</html>
```